Bright Harbor; Teaching Series Art.

Our church is going to be teaching a series of messages under the topic/title: Bright Harbor. Just looking for a simple design to help with this. I have uploaded a design that is an example of what we were thinking.

The point of the design is to communicate a new way of doing things (given some of the impact of the coronavirus) - although the background doesn't need to be too busy - just something simple, clean and modern.

Even though it's for a church, we don't need any religious art in the background (crosses, people praying, etc.) Looking for a similar feel background to the one we uploaded.

The only text should be Bright Harbor and maybe highlighting the word Bright somehow.

Font styles to use
Sans Serif

Requirements
Must have
• Title of "Bright Harbor" - no other text.

```html
<!DOCTYPE html>
<html lang="en">
<head>
<meta charset="utf-8">
<title>Bright Harbor — Teaching Series</title>
<link rel="stylesheet" href="https://fonts.googleapis.com/css2?family=Barlow:wght@300;600&display=swap">
<style>
  :root {
    --ink-deep: #0b0b0b;
    --ink-mid: #1a1a1a;
    --ink-light: #333333;
    --ink-sheen: #474747;
    --title-yellow: #ffd500;
  }
  html, body {
    margin: 0;
    padding: 0;
    width: 1200px;
    height: 1200px;
    overflow: hidden;
    background: var(--ink-deep);
  }
  .series-art {
    position: relative;
    width: 1200px;
    height: 1200px;
    overflow: hidden;
  }
  .brushed-backdrop {
    position: absolute;
    inset: 0;
    background:
      linear-gradient(45deg,
        var(--ink-mid) 0%,
        var(--ink-deep) 28%,
        var(--ink-mid) 42%,
        var(--ink-light) 56%,
        var(--ink-sheen) 66%,
        var(--ink-light) 76%,
        var(--ink-mid) 88%,
        var(--ink-light) 100%);
  }
  .series-title {
    position: absolute;
    left: 0;
    right: 0;
    top: 582px;
    transform: translateY(-50%);
    margin: 0;
    text-align: center;
    font-family: "Barlow", sans-serif;
    font-weight: 300;
    font-size: 66px;
    line-height: 1;
    letter-spacing: 0.18em;
    padding-left: 0.18em;
    color: var(--title-yellow);
    white-space: nowrap;
  }
  .series-title .title-accent {
    font-weight: 600;
  }
</style>
</head>
<body>
  <main class="series-art">
    <div class="brushed-backdrop" role="img" aria-label="Dark charcoal brushed paint texture with diagonal strokes and a soft grey sheen toward the right"></div>
    <h1 class="series-title"><span class="title-accent">BRIGHT</span> HARBOR</h1>
  </main>
</body>
</html>
```